New Business Card Design Project - RK Ledgerwise & Filing Partners, LLC

Below is a sample image of the card (TM Bookkeeping). I would like to have a designed business card that looks very similar (Front & Back). In addition, I would like to keep the same colors as well. I attached my Business Logo (RK Ledgerwise & Filing Partners, LLC) that will be on my website.

Target Market(s)

Executives, Business Owners, Board of Directors, Chief Financial Officers

Contact Information for Business Card

Font styles to use
Serif

Colors
0c5ba6
ffffff
5c5c5c

Requirements
Must have
• My Name: Malcolm Ferris, CPA
• Position: Owner
• Phone: (240) 555-0148
• Email: Mferris@rkledgerwise.example
• Website: www.Rkledgerwise.example
• Address: 4736 Ferncliff Ave #2093
• Dunmore Falls, MD 21990
Nice to have
• Same design & color scheme as TM Bookkeepnig Business card sample attached

```html
<!DOCTYPE html>
<html lang="en">
<head>
<meta charset="utf-8">
<title>RK Ledgerwise &amp; Filing Partners – Business Card</title>
<link href="https://fonts.googleapis.com/css2?family=Roboto:wght@400;500&family=Tinos&display=swap" rel="stylesheet">
<style>
  :root {
    --page-bg: #e9e9e9;
    --card-white: #f4f4f4;
    --brand-blue: #17afe0;
    --text-grey: #5c5c5c;
    --rule-grey: #9a9a9a;
    --white: #ffffff;
  }
  * { margin: 0; padding: 0; box-sizing: border-box; }
  html, body { width: 1200px; height: 960px; overflow: hidden; }
  body { background: var(--page-bg); position: relative; font-family: 'Roboto', Arial, sans-serif; }

  .card { position: absolute; width: 600px; height: 342px; }
  .card-front { left: 314px; top: 113px; background: var(--card-white); }
  .card-back { left: 311px; top: 472px; background: var(--brand-blue); }

  .brand-name {
    position: absolute; left: 46px; top: 152px;
    font-family: 'Tinos', 'Times New Roman', serif;
    font-size: 12.5px; letter-spacing: 0.3px;
    color: var(--brand-blue); text-transform: uppercase; white-space: nowrap;
  }
  .divider { position: absolute; left: 313px; top: 82px; width: 1px; height: 165px; background: var(--rule-grey); }

  .contact-block { position: absolute; left: 338px; top: 84px; color: var(--text-grey); }
  .person-name { font-size: 22px; font-weight: 500; color: var(--brand-blue); line-height: 24px; }
  .person-title { font-size: 15px; line-height: 18px; margin-bottom: 11px; }
  .address { font-size: 14.5px; line-height: 19px; margin-bottom: 8px; }
  .contact-list { list-style: none; font-size: 14.5px; line-height: 19px; }
  .contact-list li { display: flex; align-items: center; gap: 8px; }
  .contact-list svg { width: 13px; height: 13px; fill: var(--brand-blue); flex: none; }

  .back-brand {
    position: absolute; right: 40px; top: 266px; text-align: right;
    font-family: 'Tinos', 'Times New Roman', serif; color: var(--white);
  }
  .back-brand-name { font-size: 18px; letter-spacing: 1px; text-transform: uppercase; line-height: 22px; }
  .back-brand-url { font-family: 'Roboto', Arial, sans-serif; font-size: 13px; letter-spacing: 4.6px; line-height: 18px; }
</style>
</head>
<body>
  <section class="card card-front">
    <p class="brand-name">RK Ledgerwise &amp; Filing Partners</p>
    <div class="divider"></div>
    <div class="contact-block">
      <h1 class="person-name">Malcolm Ferris, CPA</h1>
      <p class="person-title">Owner</p>
      <p class="address">4736 Ferncliff Ave #2093<br>Dunmore Falls, MD 21990</p>
      <ul class="contact-list">
        <li><svg viewBox="0 0 24 24" aria-hidden="true"><path d="M6.6 10.8a15.1 15.1 0 0 0 6.6 6.6l2.2-2.2a1 1 0 0 1 1-.25 11.4 11.4 0 0 0 3.6.57 1 1 0 0 1 1 1V20a1 1 0 0 1-1 1A17 17 0 0 1 3 4a1 1 0 0 1 1-1h3.5a1 1 0 0 1 1 1c0 1.25.2 2.45.57 3.6a1 1 0 0 1-.25 1z"/></svg>(240) 555-0148</li>
        <li><svg viewBox="0 0 24 24" aria-hidden="true"><path d="M2 5h20v14H2z"/><path d="M3.5 7 12 12.5 20.5 7" fill="none" stroke="#fff" stroke-width="1.6"/></svg>Mferris@rkledgerwise.example</li>
        <li><svg viewBox="0 0 24 24" aria-hidden="true"><circle cx="12" cy="12" r="10"/><path d="M2 12h20M12 2c3 3 3 17 0 20M12 2c-3 3-3 17 0 20" fill="none" stroke="#fff" stroke-width="1.3"/></svg>www.Rkledgerwise.example</li>
      </ul>
    </div>
  </section>

  <section class="card card-back">
    <div class="back-brand">
      <p class="back-brand-name">RK Ledgerwise &amp; Filing Partners</p>
      <p class="back-brand-url">www.Rkledgerwise.example</p>
    </div>
  </section>
</body>
</html>
```